NEW YORK Plumbing/utility company 10 year anniversary business card

Looking For simple back and front business card would like to include a few things in description
We offer 24/7 emergency service
residential
commercial
industrial
municipal
services offered
Plumbing
hydro excavation
hydro jetting
Well pumps
Sewer pumps
water mains
sewer mains

```html
<!DOCTYPE html>
<html lang="en">
<head>
<meta charset="utf-8">
<title>Kestrel Creek Water &amp; Sewer – Business Card</title>
<link href="https://fonts.googleapis.com/css2?family=Poppins:wght@400;500;600;700&display=swap" rel="stylesheet">
<style>
  :root {
    --brand-blue: #1e5fd8;
    --deep-blue: #1749b4;
    --sky-blue: #4aa8f0;
    --brand-red: #e3171d;
    --ink: #1b1b1f;
    --paper: #ffffff;
    --backdrop: #e8eef6;
  }
  * { margin: 0; padding: 0; box-sizing: border-box; }
  html, body { width: 1142px; height: 1200px; overflow: hidden; }
  body {
    background: var(--backdrop);
    font-family: "Poppins", sans-serif;
    position: relative;
  }
  .card {
    position: absolute;
    left: 200px;
    width: 495px;
    height: 295px;
    background: var(--paper);
    transform: scale(1.4848);
    transform-origin: top left;
    overflow: hidden;
    box-shadow: 0 6px 16px rgba(20, 50, 110, 0.18);
  }
  .card--front { top: 134px; }
  .card--back { top: 671px; }
  .card__shapes { position: absolute; inset: 0; width: 100%; height: 100%; }

  .wordmark {
    position: absolute;
    color: var(--brand-blue);
    font-weight: 700;
    text-align: center;
    line-height: 1.1;
  }
  .wordmark__sub { display: block; letter-spacing: 0.28em; }
  .card--front .wordmark { left: 0; right: 0; top: 80px; font-size: 34px; }
  .card--front .wordmark__sub { font-size: 13px; margin-top: 6px; }

  .web-address {
    position: absolute; left: 20px; top: 232px;
    color: var(--paper); font-size: 10.5px; font-weight: 600; letter-spacing: 0.02em;
  }

  .emergency {
    position: absolute; left: 34px; top: 24px;
    color: var(--paper); font-size: 14.5px; font-weight: 600;
  }
  .sectors { position: absolute; top: 60px; left: 0; width: 100%; }
  .sector {
    position: absolute; width: 100px; margin-left: -50px; text-align: center;
    font-size: 9px; font-weight: 600; color: var(--ink);
  }
  .sector svg { display: block; margin: 0 auto 6px; width: 20px; height: 20px; }

  .services {
    position: absolute; list-style: none;
    color: var(--paper); font-size: 6px; font-weight: 500;
  }
  .services li { display: flex; align-items: center; height: 18px; }
  .services svg { width: 7px; height: 7px; margin-right: 5px; }
  .services--a { left: 32px; top: 134px; }
  .services--b { left: 132px; top: 143px; }

  .person { position: absolute; left: 322px; top: 125px; color: var(--ink); }
  .person__name { font-size: 19px; font-weight: 400; line-height: 1; }
  .person__name strong { font-weight: 700; }
  .person__role { font-size: 6.5px; font-weight: 700; margin-top: 5px; letter-spacing: 0.04em; }

  .address {
    position: absolute; left: 345px; top: 189px;
    color: var(--paper); font-size: 5.5px; line-height: 1.5; font-weight: 500;
  }
  .address-pin { position: absolute; left: 446px; top: 189px; width: 14px; height: 18px; }

  .card--back .wordmark { left: 22px; top: 230px; font-size: 15px; text-align: center; }
  .card--back .wordmark__sub { font-size: 6px; margin-top: 2px; }

  .contact {
    position: absolute; font-size: 5.5px; line-height: 1.7; color: var(--ink); font-weight: 500;
  }
  .contact--email { left: 190px; top: 238px; text-align: right; width: 78px; }
  .contact--phone { left: 355px; top: 238px; }
  .contact-icon {
    position: absolute; top: 232px; width: 30px; height: 30px; background: var(--brand-blue);
    display: flex; align-items: center; justify-content: center;
  }
  .contact-icon--email { left: 283px; }
  .contact-icon--phone { left: 438px; }
  .contact-icon svg { width: 18px; height: 18px; }
</style>
</head>
<body>

<section class="card card--front" aria-label="Business card front">
  <svg class="card__shapes" viewBox="0 0 495 295" preserveAspectRatio="none" aria-hidden="true">
    <polygon points="0,212 300,212 326,262 0,262" fill="var(--brand-blue)"/>
    <polygon points="0,262 330,262 400,232 440,232 372,295 0,295" fill="var(--brand-red)"/>
    <polygon points="495,168 495,295 370,295" fill="var(--brand-blue)"/>
    <polygon points="495,150 495,160 405,226 392,226" fill="var(--sky-blue)"/>
  </svg>
  <h1 class="wordmark">KESTREL CREEK<span class="wordmark__sub">WATER &amp; SEWER</span></h1>
  <p class="web-address">WWW.KESTRELCREEKWATER.COM</p>
</section>

<section class="card card--back" aria-label="Business card back">
  <svg class="card__shapes" viewBox="0 0 495 295" preserveAspectRatio="none" aria-hidden="true">
    <polygon points="0,0 370,0 420,50 0,50" fill="var(--brand-red)"/>
    <polygon points="370,0 495,0 495,68 438,68" fill="var(--brand-blue)"/>
    <polygon points="420,50 438,68 495,125 495,135 430,70 412,50" fill="var(--sky-blue)"/>
    <polygon points="0,122 205,122 268,220 0,220" fill="var(--brand-blue)"/>
    <polygon points="205,122 218,122 281,220 268,220" fill="var(--deep-blue)"/>
    <polygon points="238,180 495,180 495,220 262,220" fill="var(--brand-blue)"/>
  </svg>

  <p class="emergency">Emergency Service 24/7</p>

  <div class="sectors">
    <div class="sector" style="left:68px">
      <svg viewBox="0 0 20 20"><polygon points="2,9 10,2 18,9" fill="var(--brand-blue)"/><rect x="4" y="9" width="12" height="9" fill="var(--brand-blue)"/><rect x="8.5" y="12" width="3" height="6" fill="var(--brand-red)"/></svg>
      Residential
    </div>
    <div class="sector" style="left:180px">
      <svg viewBox="0 0 20 20"><rect x="3" y="3" width="8" height="15" fill="var(--brand-blue)"/><rect x="11" y="7" width="6" height="11" fill="var(--sky-blue)"/><rect x="5" y="6" width="4" height="2" fill="#fff"/><rect x="5" y="10" width="4" height="2" fill="#fff"/></svg>
      Commercial
    </div>
    <div class="sector" style="left:285px">
      <svg viewBox="0 0 20 20"><polygon points="2,18 2,10 7,13 7,10 12,13 12,4 16,4 16,18" fill="var(--brand-blue)"/><rect x="4" y="15" width="3" height="3" fill="var(--brand-red)"/></svg>
      Industrial
    </div>
    <div class="sector" style="left:383px">
      <svg viewBox="0 0 20 20"><rect x="4" y="3" width="9" height="15" fill="var(--brand-blue)"/><rect x="6" y="6" width="5" height="2" fill="#fff"/><circle cx="15" cy="14" r="4" fill="var(--brand-red)"/></svg>
      Municipal
    </div>
  </div>

  <ul class="services services--a">
    <li><svg viewBox="0 0 8 8"><polyline points="1,4 3,6.5 7,1" fill="none" stroke="#fff" stroke-width="1.4"/></svg>Plumbing</li>
    <li><svg viewBox="0 0 8 8"><polyline points="1,4 3,6.5 7,1" fill="none" stroke="#fff" stroke-width="1.4"/></svg>Hydro excavation</li>
    <li><svg viewBox="0 0 8 8"><polyline points="1,4 3,6.5 7,1" fill="none" stroke="#fff" stroke-width="1.4"/></svg>Hydro jetting</li>
    <li><svg viewBox="0 0 8 8"><polyline points="1,4 3,6.5 7,1" fill="none" stroke="#fff" stroke-width="1.4"/></svg>Well pumps</li>
  </ul>
  <ul class="services services--b">
    <li><svg viewBox="0 0 8 8"><polyline points="1,4 3,6.5 7,1" fill="none" stroke="#fff" stroke-width="1.4"/></svg>Sewer pumps</li>
    <li><svg viewBox="0 0 8 8"><polyline points="1,4 3,6.5 7,1" fill="none" stroke="#fff" stroke-width="1.4"/></svg>Water mains</li>
    <li><svg viewBox="0 0 8 8"><polyline points="1,4 3,6.5 7,1" fill="none" stroke="#fff" stroke-width="1.4"/></svg>Sewer mains</li>
  </ul>

  <div class="person">
    <p class="person__name"><strong>Marcus</strong> Bell</p>
    <p class="person__role">MANAGER</p>
  </div>

  <p class="address">420 Mill Road, Suite 5<br>Kingston, NY 12401</p>
  <svg class="address-pin" viewBox="0 0 14 18" aria-hidden="true"><path d="M7 1a5.5 5.5 0 0 0-5.5 5.5C1.5 11 7 17 7 17s5.5-6 5.5-10.5A5.5 5.5 0 0 0 7 1z" fill="#fff"/><circle cx="7" cy="6.5" r="2" fill="var(--brand-blue)"/></svg>

  <h2 class="wordmark">KESTREL CREEK<span class="wordmark__sub">WATER &amp; SEWER</span></h2>

  <p class="contact contact--email">hello@kestrelcreek.com<br>email@kestrelcreek.com</p>
  <div class="contact-icon contact-icon--email">
    <svg viewBox="0 0 18 18" aria-hidden="true"><rect x="2" y="4" width="14" height="10" fill="none" stroke="#fff" stroke-width="1.3"/><polyline points="2,4 9,10 16,4" fill="none" stroke="#fff" stroke-width="1.3"/></svg>
  </div>

  <p class="contact contact--phone">123 . 456 7890<br>123 . 456 7891</p>
  <div class="contact-icon contact-icon--phone">
    <svg viewBox="0 0 18 18" aria-hidden="true"><rect x="5" y="1.5" width="8" height="15" rx="1.5" fill="none" stroke="#fff" stroke-width="1.3"/><line x1="8" y1="14" x2="10" y2="14" stroke="#fff" stroke-width="1.3"/></svg>
  </div>
</section>

</body>
</html>
```